We are a church and would like a flyer for a special service that is held once a quarter to get families and friends to come out to join us. See below content and details for sizes.
Church Name: Covenant Harvest Global Fellowship
Church Logo : Attached
Title : Family and Friends Day
Subtitle: Strengthening Families - Connecting Relationships
Host: Bishop Kwame Dantor (file attached. Don't need full body. Please crop)
Date: Sunday, 24 May
Time: 9:30 AM
Address: 2917 Marlow Lane, Suite F, Bowie MD, 20716
Phone : 240 593 2186
Website: www.chgfellowship.org
Flyer Size: Facebook size 851 x 314 pixels, Flash size 680 x 340 & Power Point size Standard

```html
<!DOCTYPE html>
<html lang="en">
<head>
<meta charset="utf-8">
<title>Family and Friends Day – Special Service</title>
<link rel="stylesheet" href="https://fonts.googleapis.com/css2?family=Dancing+Script:wght@500;700&family=Lora:ital,wght@1,700&display=swap">
<style>
  :root {
    --sky-top: #bcd3e1;
    --sky-mid: #dfe8ec;
    --sky-haze: #eef2f3;
    --cloud: #f7f8f8;
    --ink-blue: #1f4fc4;
    --soft-blue: #7ea4df;
    --navy: #17307a;
    --host-tone: #7f858c;
  }
  html, body {
    margin: 0;
    padding: 0;
    overflow: hidden;
    background: #ffffff;
  }
  .flyer {
    position: relative;
    width: 1200px;
    height: 600px;
    overflow: hidden;
    font-family: "Dancing Script", cursive;
    color: var(--ink-blue);
  }
  .sky {
    position: absolute;
    inset: 0;
    background:
      radial-gradient(ellipse 900px 220px at 55% 108%, var(--cloud) 0%, rgba(247,248,248,0.85) 45%, rgba(247,248,248,0) 100%),
      linear-gradient(180deg, var(--sky-top) 0%, var(--sky-mid) 45%, var(--sky-haze) 70%, #e9eef0 100%);
  }
  .invite {
    position: absolute;
    left: 0;
    top: 60px;
    width: 1200px;
    height: 110px;
  }
  .invite text {
    font-family: "Dancing Script", cursive;
    font-weight: 700;
    font-size: 38px;
    fill: var(--soft-blue);
  }
  .title {
    position: absolute;
    left: 0;
    width: 1200px;
    top: 150px;
    margin: 0;
    text-align: center;
    font-weight: 700;
    font-size: 68px;
    line-height: 1;
    color: var(--ink-blue);
  }
  .subtitle {
    position: absolute;
    left: 0;
    width: 1200px;
    top: 222px;
    margin: 0;
    text-align: center;
    font-weight: 500;
    font-size: 32px;
    line-height: 1.2;
    color: var(--soft-blue);
  }
  .host-photo {
    position: absolute;
    left: 22px;
    top: 282px;
    width: 150px;
    height: 318px;
    border-radius: 64px 64px 0 0;
    background: linear-gradient(180deg, #6f747a 0%, var(--host-tone) 40%, #5d636a 100%);
  }
  .host {
    position: absolute;
    left: 178px;
    top: 312px;
    margin: 0;
    font-weight: 700;
    font-size: 30px;
    line-height: 1.4;
    color: var(--ink-blue);
  }
  .when {
    position: absolute;
    left: 680px;
    width: 440px;
    top: 330px;
    margin: 0;
    text-align: center;
    font-weight: 700;
    font-size: 50px;
    line-height: 1.22;
    color: var(--ink-blue);
  }
  .contact {
    position: absolute;
    left: 332px;
    width: 500px;
    top: 490px;
    margin: 0;
    text-align: center;
    font-family: "Lora", Georgia, serif;
    font-style: italic;
    font-weight: 700;
    font-size: 20px;
    line-height: 1.45;
    color: var(--ink-blue);
  }
  .church-name {
    position: absolute;
    left: 930px;
    top: 490px;
    width: 250px;
    display: flex;
    align-items: center;
    gap: 12px;
  }
  .church-name .dot {
    flex: none;
    width: 30px;
    height: 30px;
    border-radius: 50%;
    background: var(--navy);
  }
  .church-name span {
    font-weight: 700;
    font-size: 26px;
    line-height: 1.05;
    color: var(--navy);
  }
</style>
</head>
<body>
  <main class="flyer">
    <div class="sky" role="img" aria-label="Soft sky photograph with pale blue haze above a bank of white clouds"></div>

    <svg class="invite" viewBox="0 0 1200 110" aria-label="We Would like to invite you to a special service">
      <defs>
        <path id="invite-arc" d="M262 96 Q 620 20 990 80"/>
      </defs>
      <text><textPath href="#invite-arc" startOffset="50%" text-anchor="middle">We Would like to invite you to a special service</textPath></text>
    </svg>

    <h1 class="title">Family and Friends Day</h1>
    <p class="subtitle">Strengthening Families - Connecting Relationships</p>

    <div class="host-photo" role="img" aria-label="Photograph of Bishop Kwame Dantor in a grey suit"></div>
    <p class="host">Hosted by<br>Bishop Kwame Dantor</p>

    <p class="when">Sunday, 24 May<br>9:30 AM</p>

    <p class="contact">
      2917 Marlow Lane, Suite F, Bowie MD, 20716<br>
      (240) 593-2186<br>
      www.chgfellowship.org
    </p>

    <div class="church-name">
      <div class="dot"></div>
      <span>Covenant Harvest Global Fellowship</span>
    </div>
  </main>
</body>
</html>
```